Website Q48 coffee

I am opening a small business selling locally roasted coffee online. To start with I want a site with three pages. 1. A welcome page with logo and mission/vision. 2. Shopping/ordering page. 3. About Us page. The brand is "Q48 Coffee - Brewed with bright hearts". We are giving back to the downs syndrome community by employing people with down syndrome (Trisomy 21) and buy donating to down syndrome research.

Target Market(s)

Families and friends of people with downs syndrome

Coding

Coded - Design and coding required

Number of Pages Required

3 page

```html
<!DOCTYPE html>
<html lang="en">
<head>
<meta charset="utf-8">
<title>Q48 Coffee – Brewed with bright hearts</title>
<link href="https://fonts.googleapis.com/css2?family=Roboto:wght@300;400;500;700;900&display=swap" rel="stylesheet">
<style>
:root{
  --ink:#111111;
  --text:#333333;
  --muted:#555555;
  --line:#e3e3e3;
  --paper:#ffffff;
  --mist:#f6f6f6;
  --footer:#ececec;
  --star:#f2a019;
  --dark:#0b0b0b;
}
*{box-sizing:border-box;margin:0;padding:0}
html,body{width:1200px;height:4237px;overflow:hidden}
body{position:relative;background:var(--paper);font-family:"Roboto",Arial,sans-serif;color:var(--text)}
.abs{position:absolute}
a{color:inherit}

/* promo bar */
.promo-bar{left:0;top:0;width:1200px;height:33px;background:var(--dark);color:#fff;font-size:13px;display:flex;align-items:center;justify-content:center;gap:4px;white-space:nowrap}
.promo-bar b{font-weight:700}
.promo-bar u{margin-left:2px}

/* navigation */
.site-nav{left:0;top:33px;width:1200px;height:64px;background:#fff;border-bottom:1px solid var(--line)}
.brand{left:100px;top:9px;height:46px;display:flex;align-items:center;gap:8px;font-size:26px;font-weight:400;color:var(--ink);letter-spacing:1px;white-space:nowrap}
.brand-mark{width:14px;height:14px;border:2px solid var(--ink);flex:none}
.nav-links{left:467px;top:0;width:640px;height:64px;font-size:15px;color:var(--ink)}
.nav-links span{position:absolute;top:0;height:64px;display:flex;align-items:center;gap:5px;white-space:nowrap}
.nav-links .l1{left:0}
.nav-links .l2{left:92px}
.nav-links .l3{left:209px}
.nav-links .l4{left:318px}
.nav-links .l5{left:409px}
.nav-links .l6{left:540px}
.nav-links svg{width:18px;height:18px;stroke:var(--ink);fill:none;stroke-width:1.6;flex:none}
.nav-links .chev{width:10px;height:10px}

/* hero */
.hero{left:0;top:97px;width:1200px;height:603px;overflow:hidden;
  background:radial-gradient(ellipse at 72% 55%,#e9e2da 0 9%,#7a4a2c 16%,#3a2014 40%,#1e110a 70%),#241409}
.hero-photo{left:0;top:0;width:1200px;height:603px;
  background:linear-gradient(180deg,rgba(40,22,12,0) 55%,rgba(70,40,22,.8) 85%,#3b2114 100%),
  radial-gradient(ellipse at 95% 45%,rgba(150,115,80,.55) 0 18%,transparent 30%)}
.hero-title{left:118px;top:203px;font-size:64px;font-weight:700;color:#fff;letter-spacing:1px;white-space:nowrap}
.hero-title span{font-weight:400}
.hero-sub{left:118px;top:282px;font-size:28px;font-weight:400;color:#fff;letter-spacing:.5px;white-space:nowrap}
.hero-btn{left:118px;top:344px;width:149px;height:40px;border:2px solid #fff;color:#fff;font-size:15px;font-weight:500;display:flex;align-items:center;justify-content:center}
.hero-arrow{top:285px;width:22px;height:34px;stroke:#fff;fill:none;stroke-width:1.5}
.hero-dots{left:570px;top:565px;display:flex;gap:10px}
.hero-dots i{width:9px;height:9px;border-radius:50%;background:rgba(255,255,255,.5)}
.hero-dots i:first-child{background:#fff}

/* best sellers */
.best-sellers{left:0;top:700px;width:1190px;height:632px;background:var(--mist)}
.section-title{font-size:36px;font-weight:500;color:var(--ink);text-align:center;width:100%;white-space:nowrap}
.product-card{top:145px;width:237px;height:316px;background:#fff;border:1px solid var(--line);box-shadow:0 1px 4px rgba(0,0,0,.05);text-align:center}
.product-photo{margin:4px;height:188px;background:radial-gradient(ellipse at 50% 50%,#3a1f12 0 30%,#5b3520 42%,#f1ebe7 52%,#f4f1ef 100%)}
.product-level{margin-top:14px;font-size:11px;color:var(--muted);letter-spacing:.3px;white-space:nowrap}
.product-name{margin-top:9px;font-size:15px;color:var(--ink);font-weight:500;white-space:nowrap}
.product-price{margin-top:9px;font-size:13.5px;color:var(--ink)}
.product-rating{margin-top:10px;font-size:10px;color:var(--muted)}
.product-rating b{color:var(--star);font-weight:400;letter-spacing:1px}
.dark-btn{background:var(--dark);color:#fff;font-size:15px;font-weight:500;display:flex;align-items:center;justify-content:center;white-space:nowrap}

/* vision / mission */
.vision-photo{left:123px;top:1429px;width:449px;height:435px;border-radius:6px;
  background:radial-gradient(ellipse at 55% 60%,#1b1410 0 12%,#e7a7a9 18%,#d9c9c2 32%,#bfb8b2 60%,#8c7c6c 100%)}
.tag{height:16px;padding:0 9px;background:#3a3a3a;color:#fff;font-size:8px;display:flex;align-items:center;letter-spacing:.2px;white-space:nowrap}
.block-title{font-size:34px;color:var(--ink);font-weight:400;white-space:nowrap}
.block-title b{font-weight:700}
.block-text{font-size:14.5px;line-height:25px;color:var(--text);width:450px}

/* testimonials */
.reviews{left:0;top:1960px;width:1200px;height:557px;
  background:linear-gradient(90deg,#6f4b35 0,#c49b8a 12%,#e3e1de 22%,#ebeae8 60%,#dcdad6 100%)}
.reviews-stars{left:0;top:64px;width:1200px;text-align:center;font-size:26px;color:var(--ink);letter-spacing:2px}
.review-card{top:167px;width:316px;height:323px;background:#fff;border-radius:10px;padding:28px 22px 0 23px}
.quote-mark{font-size:78px;font-weight:900;line-height:40px;height:40px;color:var(--ink);font-family:Georgia,serif}
.review-head{margin-top:20px;font-size:13px;font-weight:500;color:var(--ink)}
.review-body{margin-top:8px;font-size:13px;line-height:24px;color:var(--text)}
.reviewer{margin-top:12px;display:flex;align-items:center;gap:10px}
.avatar{width:46px;height:46px;border-radius:50%;background:linear-gradient(160deg,#c9b9ae,#6d635d)}
.reviewer-name{font-size:13.5px;font-weight:700;color:var(--ink);white-space:nowrap}
.reviewer-name small{display:block;color:var(--star);font-size:10px;letter-spacing:1px;font-weight:400}

/* differences */
.feature-card{width:222px;background:#fff;border-radius:14px;box-shadow:0 2px 10px rgba(0,0,0,.09);text-align:center;padding:0 22px}
.feature-icon{margin:34px auto 0;width:66px;height:60px;border-radius:4px;background:linear-gradient(180deg,#d7d7d7,#9a9a9a)}
.feature-title{margin-top:14px;font-size:15px;color:var(--ink);font-weight:500;white-space:nowrap;margin-left:-14px;margin-right:-14px}
.feature-text{margin-top:14px;font-size:11.5px;line-height:20px;color:var(--text)}
.tools-photo{left:123px;top:2938px;width:222px;height:238px;border-radius:14px;
  background:linear-gradient(160deg,#b9b7b2 0,#8d8a85 40%,#3b2a20 75%,#6f6a64 100%)}
.diff-title{left:666px;top:2718px;font-size:28px;color:var(--ink);font-weight:500;white-space:nowrap}
.diff-title span{font-weight:400}
.diff-text{left:666px;top:2781px;width:410px;font-size:11.5px;line-height:25px;color:var(--text)}
.journey-art{left:99px;top:3230px;width:1002px;height:264px;
  background:linear-gradient(180deg,#ffffff,#f3f3f3 70%,#ffffff)}

/* newsletter */
.scoop-title{left:0;top:3573px;width:1200px;text-align:center;font-size:32px;color:var(--ink);font-weight:700;white-space:nowrap}
.scoop-title span{font-weight:400}
.scoop-sub{left:0;top:3625px;width:1200px;text-align:center;font-size:14px;color:var(--ink)}
.email-field{left:357px;top:3666px;width:371px;height:45px;border:1px solid #cfcfcf;font-size:12px;color:var(--text);display:flex;align-items:center;padding-left:16px}

/* footer */
.site-footer{left:0;top:3747px;width:1200px;height:490px;background:linear-gradient(180deg,#eeeeee,#e7e7e7)}
.footer-brand{left:100px;top:75px;width:153px;height:155px;display:flex;align-items:center;justify-content:center;gap:7px;font-size:21px;color:var(--ink);font-weight:400;white-space:nowrap}
.footer-col{top:84px}
.footer-col h4{font-size:16px;font-weight:700;color:var(--ink);margin-bottom:10px;white-space:nowrap}
.footer-col li{list-style:none;font-size:13.5px;line-height:28px;color:var(--ink);white-space:nowrap}
.social{display:flex;gap:10px;margin-top:8px}
.social i{width:34px;height:34px;border-radius:50%;background:#fff;border:1px solid #ddd}
.footer-rule{left:100px;top:280px;width:1000px;height:1px;background:#d5d5d5}
.copyright{left:100px;top:289px;font-size:13px;color:var(--ink);white-space:nowrap}
.pay-row{left:758px;top:288px;display:flex;gap:9px}
.pay-row i{width:30px;height:18px;border-radius:2px;background:#c9c9cf}
.beans-band{left:0;top:310px;width:1200px;height:180px;
  background:linear-gradient(180deg,rgba(231,231,231,0) 0,rgba(90,52,30,.5) 30%,#3b2012 60%,#24120a 100%)}
</style>
</head>
<body>

<div class="abs promo-bar"><b>Save 5%</b> With Subscription Orders <u>Learn more</u></div>

<header class="abs site-nav">
  <div class="abs brand"><span class="brand-mark"></span>Q48 COFFEE</div>
  <nav class="abs nav-links">
    <span class="l1">Home</span>
    <span class="l2">Shopping</span>
    <span class="l3">About Us</span>
    <span class="l4"><svg viewBox="0 0 20 20"><path d="M3 12V9a7 7 0 0 1 14 0v3"/><rect x="2" y="11" width="4" height="5" rx="1"/><rect x="14" y="11" width="4" height="5" rx="1"/></svg>Help<svg class="chev" viewBox="0 0 10 10"><path d="M2 4l3 3 3-3"/></svg></span>
    <span class="l5"><svg viewBox="0 0 20 20"><circle cx="10" cy="7" r="4"/><path d="M3 18c1-4 4-6 7-6s6 2 7 6"/></svg>My Account</span>
    <span class="l6"><svg viewBox="0 0 20 20"><path d="M1 3h3l2 10h10l2-7H5"/><circle cx="8" cy="17" r="1.3"/><circle cx="15" cy="17" r="1.3"/></svg>My Cart<svg class="chev" viewBox="0 0 10 10"><path d="M2 4l3 3 3-3"/></svg></span>
  </nav>
</header>

<section class="abs hero">
  <div class="abs hero-photo" role="img" aria-label="Cup of coffee with heart-shaped steam on a saucer, surrounded by roasted beans and a burlap sack"></div>
  <h1 class="abs hero-title">Q48 <span>COFFEE</span></h1>
  <p class="abs hero-sub">BREWED WITH BRIGHT HEARTS</p>
  <div class="abs hero-btn">SHOP NOW</div>
  <svg class="abs hero-arrow" style="left:62px" viewBox="0 0 22 34"><path d="M18 2L4 17l14 15"/></svg>
  <svg class="abs hero-arrow" style="left:1116px" viewBox="0 0 22 34"><path d="M4 2l14 15L4 32"/></svg>
  <div class="abs hero-dots"><i></i><i></i><i></i></div>
</section>

<section class="abs best-sellers">
  <h2 class="abs section-title" style="top:74px">BEST SELLERS</h2>
  <article class="abs product-card" style="left:100px">
    <div class="product-photo" role="img" aria-label="Pile of light roast coffee beans"></div>
    <p class="product-level">LIGHT ROAST LERVEL</p>
    <p class="product-name">Morning Hearth House Blend</p>
    <p class="product-price">$10.55 - $19.75/lb</p>
    <p class="product-rating"><b>★★★★★</b> (24 reviews)</p>
  </article>
  <article class="abs product-card" style="left:355px">
    <div class="product-photo" role="img" aria-label="Pile of medium roast coffee beans"></div>
    <p class="product-level">MEDIUM ROAST LERVEL</p>
    <p class="product-name">Morning Hearth House Blend</p>
    <p class="product-price">$10.55 - $19.75/lb</p>
    <p class="product-rating"><b>★★★★★</b> (24 reviews)</p>
  </article>
  <article class="abs product-card" style="left:608px">
    <div class="product-photo" role="img" aria-label="Pile of medium dark roast coffee beans"></div>
    <p class="product-level">MEDIUM DARK ROAST LERVEL</p>
    <p class="product-name">Morning Hearth House Blend</p>
    <p class="product-price">$10.55 - $19.75/lb</p>
    <p class="product-rating"><b>★★★★★</b> (24 reviews)</p>
  </article>
  <article class="abs product-card" style="left:861px">
    <div class="product-photo" role="img" aria-label="Pile of dark roast coffee beans"></div>
    <p class="product-level">DARK ROAST LERVEL</p>
    <p class="product-name">Morning Hearth House Blend</p>
    <p class="product-price">$10.55 - $19.75/lb</p>
    <p class="product-rating"><b>★★★★★</b> (24 reviews)</p>
  </article>
  <div class="abs dark-btn" style="left:498px;top:498px;width:204px;height:48px">ALL ROASTED COFFEE</div>
</section>

<section>
  <div class="abs vision-photo" role="img" aria-label="Pink cup of black coffee on a saucer with scattered beans and coffee cherries on a white wooden table"></div>
  <div class="abs tag" style="left:633px;top:1472px">WHAT WE ASPIRE TO BE</div>
  <h2 class="abs block-title" style="left:632px;top:1494px"><b>OUR</b> VISION</h2>
  <p class="abs block-text" style="left:633px;top:1537px">Develop A Company That Marketas Coffee And Related Products To Family And Friends Of The Down Syndrome Community</p>
  <div class="abs tag" style="left:633px;top:1626px">WHO WE ARE, WHAT WE DO</div>
  <h2 class="abs block-title" style="left:632px;top:1648px"><b>OUR</b> MISSION</h2>
  <p class="abs block-text" style="left:633px;top:1691px">create and grow an online company selling contract roasted coffee. as growth permits become a fully vertically integrated coffee company from roasting to our own coffee shop. The company will give significant funds to medical research in downs syndrome and we will hire as many people with Downs syndrome as possible.</p>
</section>

<section class="abs reviews" role="img" aria-label="Hands holding cups of coffee over a whitewashed wooden table">
  <div class="abs reviews-stars">★★★★★</div>
  <h2 class="abs section-title" style="top:100px;font-size:31px;font-weight:500">REAL CUSTOMERS ABOUT US</h2>
  <article class="abs review-card" style="left:100px">
    <div class="quote-mark">“</div>
    <p class="review-head">WONDERFUL BUSINESS</p>
    <p class="review-body">Lorem ipsum dolor sit amet, cetur adipiscing elit, sed do eiusmod tempor ididunt ut labore et dolore magna aliqua. is ipsum suspendisse ultrices gravida. Risus codo viverra maecenas accumsan lacus vel facilisis.</p>
    <div class="reviewer"><div class="avatar" role="img" aria-label="Customer portrait"></div><p class="reviewer-name">- Maya Linden<small>★★★★★</small></p></div>
  </article>
  <article class="abs review-card" style="left:442px">
    <div class="quote-mark">“</div>
    <p class="review-head">WONDERFUL BUSINESS</p>
    <p class="review-body">Lorem ipsum dolor sit amet, cetur adipiscing elit, sed do eiusmod tempor ididunt ut labore et dolore magna aliqua. is ipsum suspendisse ultrices gravida. Risus codo viverra maecenas accumsan lacus vel facilisis.</p>
    <div class="reviewer"><div class="avatar" role="img" aria-label="Customer portrait"></div><p class="reviewer-name">- Maya Linden<small>★★★★★</small></p></div>
  </article>
  <article class="abs review-card" style="left:784px">
    <div class="quote-mark">“</div>
    <p class="review-head">WONDERFUL BUSINESS</p>
    <p class="review-body">Lorem ipsum dolor sit amet, cetur adipiscing elit, sed do eiusmod tempor ididunt ut labore et dolore magna aliqua. is ipsum suspendisse ultrices gravida. Risus codo viverra maecenas accumsan lacus vel facilisis.</p>
    <div class="reviewer"><div class="avatar" role="img" aria-label="Customer portrait"></div><p class="reviewer-name">- Maya Linden<small>★★★★★</small></p></div>
  </article>
</section>

<section>
  <article class="abs feature-card" style="left:123px;top:2647px;height:265px">
    <div class="feature-icon" role="img" aria-label="Line icon of a coffee bag and beans"></div>
    <p class="feature-title">Hand-packed goods</p>
    <p class="feature-text">We control every part of the fulfillment process, from roast to post. Every hand-packed bag is filled with the exceptional coffee you deserve.</p>
  </article>
  <div class="abs tools-photo" role="img" aria-label="Latte art cup, ground coffee and beans in portafilters on a grey surface"></div>
  <article class="abs feature-card" style="left:391px;top:2594px;height:265px">
    <div class="feature-icon" role="img" aria-label="Line icon of a coffee grinder"></div>
    <p class="feature-title">Fresh Roasted Coffee</p>
    <p class="feature-text">Even the highest grade coffee will taste bad if it is old. With that concern in mind, we roast our craft coffees all day long.</p>
  </article>
  <article class="abs feature-card" style="left:391px;top:2875px;height:263px">
    <div class="feature-icon" role="img" aria-label="Line icon of a roastery storefront"></div>
    <p class="feature-title">From roaster to customers</p>
    <p class="feature-text">By trading directly with you online, we ensure orders travel straight from our roaster to your doorstep. That way, your coffee arrives as close to its roast date as possible.</p>
  </article>
  <h2 class="abs diff-title">WHAT MAKES <span>US DIFFERENT?</span></h2>
  <p class="abs diff-text">Lorem ipsum dolor sit amet, consectetur adipiscit, sed do eiusmod tempor incididunt ut labore et dolore magna aliqua. Quissum suspendisse ultrices gravida. Risus commodo viverra maecenaumsan lacus vel facilisis. Lorem ipsum dolor sit amet, consectetur adipiscid do eiusmod tempor incididunt ut labore et dolore magna aliqua. Quis ipsum suspendisse ultrices gravida. Risus commodo viverra maecenas accumsan lacus vel facilisis.</p>
  <div class="abs dark-btn" style="left:666px;top:2951px;width:204px;height:46px">READ MORE ABOUT US</div>
  <div class="abs journey-art" role="img" aria-label="Line drawing of the coffee journey: roaster, packer, delivery van, barista pouring and a customer enjoying a cup"></div>
</section>

<section>
  <h2 class="abs scoop-title">GET THE <span>SCOOP</span></h2>
  <p class="abs scoop-sub">Sign up for the newsletter and receive discounts, coupons &amp; more</p>
  <div class="abs email-field">Your email address</div>
  <div class="abs dark-btn" style="left:741px;top:3666px;width:102px;height:45px">SUBMIT</div>
</section>

<footer class="abs site-footer">
  <div class="abs footer-brand"><span class="brand-mark"></span>Q48 COFFEE</div>
  <div class="abs footer-col" style="left:353px"><h4>QUICK LINKS</h4><ul><li>Home</li><li>Shopping</li><li>About Us</li><li>Contact</li></ul></div>
  <div class="abs footer-col" style="left:556px"><h4>HELP &amp; FAQ</h4><ul><li>FAQs</li><li>Returns</li><li>Contact Us</li><li>Chek Order Status</li><li>Accessibility</li></ul></div>
  <div class="abs footer-col" style="left:766px"><h4>COMPANY</h4><ul><li>Careers</li><li>Affiliates</li><li>Terms &amp; Conditions</li><li>Privacy</li><li>Privacy Rights</li></ul></div>
  <div class="abs footer-col" style="left:981px"><h4>CONNECT</h4><div class="social"><i aria-label="Social link"></i><i aria-label="Social link"></i><i aria-label="Social link"></i></div></div>
  <div class="abs footer-rule"></div>
  <div class="abs beans-band" role="img" aria-label="Roasted coffee beans with green coffee leaves"></div>
  <p class="abs copyright">©Copyright ©2021 Q48 coffee. All Rights Reserved.</p>
  <div class="abs pay-row" aria-label="Accepted payment methods"><i></i><i></i><i></i><i></i><i></i><i></i><i></i><i></i><i></i></div>
</footer>

</body>
</html>
```